A reimagined website for a cross-border tax firm

There are two aspects to this project for Brindlemoor Tax Advisory:
1) I need a logo update to accommodate increasing focus and specialization in my business. The byline under the name “Brindlemoor Tax Advisory” needs to change:
ORIGINAL: TAX SUPPORT FOR PUBLIC ACCOUNTING FIRMS
REVISED: CROSS-BORDER TAX SERVICES • U.S. & CANADA
2) I need a website “refresh” (see current website at www.levyhelpdesk.example) based on this logo – a new vision for a website with greater clarity, focus and organization. It should represent a re-envisioning of the current approach, and not the wholesale abandonment of the style represented there. I need it to be creative, compelling and attention grabbing, but still professional. This should, at a minimum, update any places where the old name/logo is used, but I want the redesign to go beyond this to something more intuitive. I need high quality separate PNG files of the various logo styles for use in various documents, but HTML coding would be a helpful but not necessary addition.

Target Market(s)

People in need of cross-border tax services - Canada and US

Coding

Number of Pages Required

Requirements
Must have
• Greater crispness, sharpness - higher resolution
• A more compelling, organized approach - make the wording and images more accessible to the website user (especially the staff bios, which have scroll bars now)
Nice to have
• Replacement of stock image with a true image of the Halifax skyline
Should not have
• Deviate from colour pattern represented in website logo of blue/orange
• Deviate from existing logo except for word replacement

```html
<!DOCTYPE html>
<html lang="en">
<head>
<meta charset="utf-8">
<title>Brindlemoor Tax Advisory</title>
<link rel="stylesheet" href="https://fonts.googleapis.com/css2?family=Cinzel:wght@400;600&family=Source+Serif+4:wght@400&display=swap">
<style>
:root{
  --white:#ffffff;
  --gold:#f0b43c;
  --tile-team:#1f8acd;
  --tile-firms:#1f6fc4;
  --tile-individuals:#1b4d9c;
  --tile-payment:#1e2f66;
  --footer:#1b1b1d;
  --footer-gold:#e3a62a;
}
*{margin:0;padding:0;box-sizing:border-box}
html,body{width:1200px;height:688px;overflow:hidden;background:var(--footer)}
body{font-family:"Source Serif 4",Georgia,serif;color:var(--white);position:relative}
.hero{position:absolute;left:0;top:0;width:1200px;height:525px;
  background:linear-gradient(160deg,#2a4f8f 0%,#1c3f86 35%,#2458ad 60%,#1a3c7c 100%)}
.hero::after{content:"";position:absolute;inset:0;
  background:radial-gradient(ellipse at 50% 40%,rgba(40,100,200,.35),rgba(10,30,80,.25) 70%)}
.hero-content{position:absolute;inset:0;z-index:1}
.nav{position:absolute;top:20px;left:0;width:100%;display:flex;justify-content:center;gap:20px;
  font-family:"Cinzel",serif;font-size:14px;letter-spacing:.3px}
.nav a{color:var(--white);text-decoration:none}
.nav a.active{color:var(--gold)}
.brand-mark{position:absolute;left:547px;top:117px;width:105px;height:105px;background:var(--white)}
.title{position:absolute;left:0;width:100%;text-align:center;top:232px;
  font-family:"Cinzel",serif;font-weight:600;font-size:47px;letter-spacing:1px}
.rule{position:absolute;left:265px;top:291px;width:668px;height:2px;background:var(--white)}
.subtitle{position:absolute;left:0;width:100%;text-align:center;top:296px;
  font-family:"Cinzel",serif;font-size:29px;letter-spacing:.5px}
.intro{position:absolute;left:270px;width:660px;top:346px;text-align:center;font-size:12.5px;line-height:14.5px}
.cta{position:absolute;left:523px;top:403px;width:157px;height:45px;border:1px solid var(--white);
  display:flex;align-items:center;justify-content:center;font-family:"Cinzel",serif;font-size:15px;color:var(--white);text-decoration:none}
.tiles{position:absolute;left:0;top:525px;width:1200px;height:118px;display:flex}
.tile{width:300px;height:118px;position:relative;padding-left:39px;display:flex;flex-direction:column;justify-content:center}
.tile svg{position:absolute;left:10px;top:49px}
.tile h2{font-family:"Cinzel",serif;font-weight:600;font-size:15px;margin-bottom:3px}
.tile p{font-size:9px;line-height:11px;width:235px}
.tile-team{background:var(--tile-team)}
.tile-firms{background:var(--tile-firms);padding-left:49px}
.tile-individuals{background:var(--tile-individuals);padding-left:46px}
.tile-payment{background:var(--tile-payment);padding-left:57px}
.tile-firms svg,.tile-individuals svg{left:16px}
.tile-payment svg{left:18px}
.footer{position:absolute;left:0;top:643px;width:1200px;height:45px;background:var(--footer);color:var(--footer-gold)}
.footer-brand{position:absolute;left:42px;top:10px;display:flex;align-items:center;gap:8px}
.footer-square{width:25px;height:25px;background:var(--footer-gold)}
.footer-name{font-family:"Cinzel",serif;font-size:14.5px;line-height:15px}
.footer-name small{display:block;font-size:8.5px;line-height:10px}
.footer-item{position:absolute;top:17px;font-size:9.5px;display:flex;align-items:center;gap:5px}
</style>
</head>
<body>
<section class="hero" role="img" aria-label="Upward view of glass office towers in a blue tint"></section>
<div class="hero-content">
  <nav class="nav">
    <a class="active" href="#">Home</a><a href="#">Our Team</a><a href="#">For Public Accounting Firms</a><a href="#">For Individuals</a><a href="#">Contact</a><a href="#">Payment</a>
  </nav>
  <div class="brand-mark"></div>
  <h1 class="title">BRINDLEMOOR TAX ADVISORY</h1>
  <div class="rule"></div>
  <div class="subtitle">CROSS-BORDER TAX SERVICES • U.S. &amp; CANADA</div>
  <p class="intro">We are firm devoted to helping individuals and businesses determine, comply with and minimize/optimize their Canadian and U.S. tax obligations. Let’s take a moment to unpack that sentence.</p>
  <a class="cta" href="#">CONTACT US</a>
</div>
<section class="tiles">
  <div class="tile tile-team">
    <svg width="16" height="28" viewBox="0 0 16 28"><path d="M2 2 L14 14 L2 26" fill="none" stroke="#fff" stroke-width="2"/></svg>
    <h2>OUR TEAM</h2>
    <p>Educated at Northgate University and Ashcombe University, he began his career in the Riverton office of Calder</p>
  </div>
  <div class="tile tile-firms">
    <svg width="16" height="28" viewBox="0 0 16 28"><path d="M2 2 L14 14 L2 26" fill="none" stroke="#fff" stroke-width="2"/></svg>
    <h2>PUBLIC ACCOUNTING FIRMS</h2>
    <p>We provide a range of services to Canadian public accounting firms (PAFs) to assist them in serving their clients.</p>
  </div>
  <div class="tile tile-individuals">
    <svg width="16" height="28" viewBox="0 0 16 28"><path d="M2 2 L14 14 L2 26" fill="none" stroke="#fff" stroke-width="2"/></svg>
    <h2>INDIVIDUALS</h2>
    <p>We are firm devoted to helping individuals and businesses determine, comply with and minimize /optimize their Canadian and U.S. tax obligations.</p>
  </div>
  <div class="tile tile-payment">
    <svg width="16" height="28" viewBox="0 0 16 28"><path d="M2 2 L14 14 L2 26" fill="none" stroke="#fff" stroke-width="2"/></svg>
    <h2>PAYMENT</h2>
    <p>Sell and acquire offices, shops and industrial property on Landlords and Corporate Clients.</p>
  </div>
</section>
<footer class="footer">
  <div class="footer-brand">
    <div class="footer-square"></div>
    <div class="footer-name">BRINDLEMOOR TAX ADVISORY<small>CROSS-BORDER TAX SERVICES • U.S. &amp; CANADA</small></div>
  </div>
  <div class="footer-item" style="left:483px">
    <svg width="8" height="8" viewBox="0 0 8 8"><path d="M1 1 L3 1 L3.6 2.8 L2.6 3.5 Q3.5 5 4.5 5.4 L5.2 4.4 L7 5 L7 7 Q2 7 1 1Z" fill="#e3a62a"/></svg>
    (902) 555-0147
  </div>
  <div class="footer-item" style="left:594px">
    <svg width="10" height="8" viewBox="0 0 10 8"><rect x="0" y="0" width="10" height="8" fill="#e3a62a"/><path d="M0 0 L5 4.5 L10 0" fill="none" stroke="#1b1b1d" stroke-width="1"/></svg>
    Email: info@levyhelpdesk.example
  </div>
  <div class="footer-item" style="left:1009px">© 2017 Brindlemoor Tax Advisory</div>
</footer>
</body>
</html>
```